Business card design needed

This is a new business and a unique service.
The market is academic staff at universities in Australia.
The services include workshops, seminars, individual research planning, individual support to develop grant applications for major funding. I will travel to work with people or work electronically with individuals. I have a highly successful track record and am known in many universities for work done in the past.

Target Market(s)

university professorial staff and junior academic staff in australia

Industry/Entity Type

Travel

Contact Information for Business Card

The Scholar Summit
Charting Roads to Scholar Funding

Dr Lorna P Quist

www.scholarsummit.com.au
E: info@scholarsummit.com.au
Ph: 0487 620843

Requirements
Must have
• I want a classic simple design. Colours - clean shades of blue with a contrast (not browns or orange).
I want to see line used as the primary feature, diagonal or other acute angles through part of the card.
Fonts should be crisp, angular and highly readable. Use upper and lower case in all text (except email and web address)
A simple logo based on TSS would be good.
Card can be designed vertically if the design works best that way.

```html
<!DOCTYPE html>
<html lang="en">
<head>
<meta charset="utf-8">
<title>The Scholar Summit – Business Card</title>
<link href="https://fonts.googleapis.com/css2?family=Source+Sans+3:wght@400;600&display=swap" rel="stylesheet">
<style>
  :root {
    --page-bg: #e9ebee;
    --navy: #0d3a78;
    --deep-navy: #0a2a5c;
    --brand-blue: #0f4a8a;
    --accent-blue: #1a6fc2;
    --sky: #1fa6d8;
    --silver-light: #f4f4f4;
    --silver-mid: #dcdcdc;
    --silver-dark: #b9b9b9;
    --ink: #1e1e1e;
    --ink-soft: #3a3a3a;
    --white: #ffffff;
  }
  * { margin: 0; padding: 0; box-sizing: border-box; }
  html, body {
    width: 1200px; height: 900px; overflow: hidden;
    background: var(--page-bg);
    font-family: "Source Sans 3", "Myriad Pro", Arial, sans-serif;
  }
  .canvas { position: relative; width: 1200px; height: 900px; }

  .card {
    position: absolute;
    width: 568px; height: 318px;
    overflow: hidden;
    box-shadow: 0 3px 10px rgba(0,0,0,0.18);
  }
  .card-front {
    left: 45px; top: 160px;
    background: linear-gradient(125deg, var(--silver-dark) 0%, var(--silver-mid) 30%, var(--silver-light) 48%, var(--silver-mid) 66%, var(--silver-dark) 100%);
  }
  .card-back {
    left: 590px; top: 520px;
    background:
      radial-gradient(ellipse 60% 45% at 62% 62%, var(--sky) 0%, rgba(31,166,216,0.35) 45%, rgba(31,166,216,0) 75%),
      linear-gradient(135deg, var(--deep-navy) 0%, var(--navy) 45%, var(--deep-navy) 100%);
  }
  .edge-band { position: absolute; left: 0; top: 0; width: 568px; height: 60px; }

  .wordmark {
    position: absolute;
    font-weight: 600;
    font-size: 19px;
    letter-spacing: 0.5px;
    line-height: 1;
  }
  .tagline {
    position: absolute;
    font-size: 14.5px;
    line-height: 1;
  }
  .card-front .wordmark { left: 45px; top: 72px; color: var(--brand-blue); }
  .card-front .tagline { left: 45px; top: 98px; color: var(--ink-soft); }
  .card-back .wordmark { left: 130px; top: 134px; color: var(--white); }
  .card-back .tagline { left: 130px; top: 162px; color: #dbe9f7; font-size: 17px; }

  .contact {
    position: absolute;
    right: 45px; top: 170px;
    text-align: right;
    color: var(--ink);
  }
  .contact .person { font-size: 25px; line-height: 32px; }
  .contact .line { font-size: 18.5px; line-height: 26px; }
  .contact .label { color: var(--accent-blue); font-weight: 600; }
</style>
</head>
<body>
<main class="canvas">

  <section class="card card-front" aria-label="Business card front">
    <svg class="edge-band" viewBox="0 0 568 60" aria-hidden="true">
      <defs>
        <linearGradient id="bandNavy" x1="0" y1="0" x2="1" y2="0">
          <stop offset="0" stop-color="#0d3a78" stop-opacity="0"/>
          <stop offset="0.45" stop-color="#0d3a78" stop-opacity="0.7"/>
          <stop offset="1" stop-color="#0a2a5c"/>
        </linearGradient>
        <linearGradient id="bandLight" x1="0" y1="0" x2="1" y2="0">
          <stop offset="0" stop-color="#ffffff" stop-opacity="0"/>
          <stop offset="0.6" stop-color="#ffffff" stop-opacity="0.9"/>
          <stop offset="1" stop-color="#ffffff" stop-opacity="0.4"/>
        </linearGradient>
      </defs>
      <polygon points="30,0 568,0 568,4 120,40" fill="url(#bandNavy)"/>
      <polygon points="150,34 568,4 568,7 230,32" fill="url(#bandLight)"/>
    </svg>
    <div class="wordmark">The Scholar Summit</div>
    <div class="tagline">Charting Roads to Scholar Funding</div>
    <div class="contact">
      <div class="person">Dr Lorna P Quist</div>
      <div class="line">www.scholarsummit.com.au</div>
      <div class="line"><span class="label">E:</span> info@scholarsummit.com.au</div>
      <div class="line"><span class="label">P:</span> 0487 620843</div>
    </div>
  </section>

  <section class="card card-back" aria-label="Business card back">
    <svg class="edge-band" viewBox="0 0 568 60" aria-hidden="true">
      <defs>
        <linearGradient id="bandWhite" x1="0" y1="0" x2="1" y2="0">
          <stop offset="0" stop-color="#ffffff" stop-opacity="0"/>
          <stop offset="0.5" stop-color="#ffffff" stop-opacity="0.85"/>
          <stop offset="1" stop-color="#ffffff"/>
        </linearGradient>
        <linearGradient id="bandPale" x1="0" y1="0" x2="1" y2="0">
          <stop offset="0" stop-color="#9cc6ec" stop-opacity="0"/>
          <stop offset="1" stop-color="#9cc6ec" stop-opacity="0.6"/>
        </linearGradient>
      </defs>
      <polygon points="30,0 568,0 568,6 120,40" fill="url(#bandWhite)"/>
      <polygon points="150,36 568,6 568,10 230,34" fill="url(#bandPale)"/>
    </svg>
    <div class="wordmark">The Scholar Summit</div>
    <div class="tagline">Charting Roads to Scholar Funding</div>
  </section>

</main>
</body>
</html>
```